Silver Ridge Harlow Basin Masters Week of Golf 2107

I would like a design for an A4 Event Flyer.

This is a golf event for Senior ladies and gentlemen. I would like the design to appeal to an older age group.

I would like somewhere on the flyer a golf ball image with the following details inside "Please put me on your notice board"

The information on the Flyer is as follows
- (Title - Silver ridge Harlow Basin Masters Week of Golf 2017)
- Date 16th of October to 20th of October
- Over 55 years of age
- We invite our fellow Veteran Ladies and Gentlemen to play a unique 54 hole stableford event at three fantastic Golf Courses, and finish the week at Penwick Golf club with a 2BBB Medley.
- Insert schedule that is attached in PDF. They layout can be changed.

- For entry form and details
Contact: Penwick Proshop on 02 69318842 or email admin@penwickdalbrookgolf.example.au

I have attached 4 golf course images. This is a photo of each course. Could I please get these added to the flyer.

Target Market(s)

seniors

Industry/Entity Type

Golf Course

Requirements
Must have
• All information provided

```html
<!DOCTYPE html>
<html lang="en">
<head>
<meta charset="UTF-8">
<title>Silver ridge Harlow Basin Masters Week of Golf 2017</title>
<link rel="stylesheet" href="https://fonts.googleapis.com/css2?family=Source+Sans+3:ital,wght@0,400;0,500;0,600;0,700;1,400&display=swap">
<style>
  :root {
    --navy: #2c2e8c;
    --green: #8db443;
    --panel: #4f6db3;
    --month: #8fc043;
    --day: #2c2e8c;
    --white: #ffffff;
    --ink: #111111;
    --ball-shade: #d7dde6;
  }
  * { margin: 0; padding: 0; box-sizing: border-box; }
  html, body { width: 848px; height: 1200px; overflow: hidden; }
  body { font-family: "Source Sans 3", sans-serif; background: var(--white); }
  .flyer { position: relative; width: 848px; height: 1200px; overflow: hidden; }

  .hero {
    position: absolute; left: 0; top: 0; width: 848px; height: 566px;
    background: linear-gradient(180deg, #2f7fd0 0%, #5ea3e4 35%, #9cc7ea 60%, #b9cfdf 80%, #8fa6b8 100%);
  }
  .hero-people {
    position: absolute; left: 0; top: 20px; width: 640px; height: 546px;
    background: radial-gradient(ellipse at 45% 55%, #e6eef4 0%, #c9d9e6 45%, rgba(180,200,215,0) 75%);
  }
  .hero-palms {
    position: absolute; right: 0; top: 60px; width: 360px; height: 506px;
    background: radial-gradient(ellipse at 60% 40%, rgba(70,110,60,.55) 0%, rgba(70,110,60,0) 70%);
  }
  .event-title {
    position: absolute; top: 13px; left: 0; width: 848px; text-align: center;
    color: var(--white); font-weight: 700; font-size: 28px; line-height: 36px;
    text-shadow: 0 1px 4px rgba(0,0,0,.35); white-space: nowrap;
  }
  .invitation {
    position: absolute; top: 401px; left: 0; width: 848px; text-align: center;
    color: var(--white); font-weight: 600; font-size: 31px; line-height: 41px;
    white-space: nowrap; text-shadow: 0 1px 5px rgba(0,0,0,.45);
  }

  .notice-ball { position: absolute; left: 660px; top: 72px; width: 160px; height: 160px; }
  .notice-ball svg { position: absolute; inset: 0; }
  .notice-ball p {
    position: absolute; left: 22px; top: 42px; width: 116px; text-align: center;
    color: var(--navy); font-weight: 700; font-size: 17px; line-height: 20px;
  }

  .band { position: absolute; left: 0; width: 848px; text-align: center; color: var(--white); font-size: 24px; font-weight: 500; }
  .band-dates { top: 566px; height: 53px; line-height: 53px; background: var(--navy); }
  .band-age { top: 619px; height: 54px; line-height: 54px; background: var(--green); }

  .program { position: absolute; left: 0; top: 673px; width: 848px; height: 320px; background: var(--panel); }
  .program h2 {
    position: absolute; top: 10px; left: 0; width: 848px; text-align: center;
    font-size: 23px; line-height: 26px; font-weight: 700; color: var(--ink);
  }
  .row { position: absolute; left: 0; width: 848px; }
  .row .month { position: absolute; left: 100px; top: 0; font-size: 19px; font-weight: 500; color: var(--month); line-height: 24px; }
  .row .date {
    position: absolute; left: 140px; top: -4px; width: 32px; height: 32px; border-radius: 50%;
    background: var(--month); color: var(--ink); font-size: 18px; font-weight: 500; line-height: 32px; text-align: center;
  }
  .row .day { position: absolute; width: 50px; left: 186px; top: 0; text-align: center; font-size: 19px; font-weight: 500; color: var(--day); line-height: 24px; }
  .row .detail { position: absolute; left: 250px; top: 2px; font-size: 16px; font-weight: 500; color: var(--white); line-height: 21px; white-space: nowrap; }

  .courses { position: absolute; left: 0; top: 993px; width: 848px; height: 153px; display: flex; }
  .course { flex: 1; height: 100%; }
  .course-1 { background: linear-gradient(180deg, #7fb5e6 0%, #9fc3d8 35%, #5e8c3c 60%, #74a43e 100%); }
  .course-2 { background: linear-gradient(180deg, #4f8fd6 0%, #4b7a3d 40%, #a07c3a 75%, #7e8e3a 100%); }
  .course-3 { background: linear-gradient(180deg, #3f6b35 0%, #6fa040 40%, #86b548 100%); }
  .course-4 { background: linear-gradient(180deg, #9cc0db 0%, #4d7a35 40%, #7eb04a 75%, #9ac468 100%); }
  .tagline {
    position: absolute; left: 0; top: 1122px; width: 848px; text-align: center;
    color: var(--white); font-style: italic; font-size: 18px; line-height: 22px;
    text-shadow: 0 1px 3px rgba(0,0,0,.5); white-space: nowrap;
  }

  .contact {
    position: absolute; left: 0; top: 1146px; width: 848px; height: 54px; line-height: 54px;
    background: var(--navy); color: var(--white); text-align: center; font-weight: 700; font-size: 18px; white-space: nowrap;
  }
</style>
</head>
<body>
<div class="flyer">
  <div class="hero" role="img" aria-label="Photo of a smiling senior couple holding golf clubs under palm trees and a blue sky">
    <div class="hero-people"></div>
    <div class="hero-palms"></div>
  </div>
  <h1 class="event-title">Silver ridge Harlow Basin Masters Week of Golf 2017</h1>

  <div class="notice-ball">
    <svg width="160" height="160" viewBox="0 0 160 160" aria-hidden="true">
      <defs>
        <radialGradient id="ballShade" cx="38%" cy="34%" r="70%">
          <stop offset="0%" stop-color="#ffffff"/>
          <stop offset="70%" stop-color="#f3f5f8"/>
          <stop offset="100%" stop-color="var(--ball-shade)"/>
        </radialGradient>
      </defs>
      <circle cx="80" cy="80" r="76" fill="url(#ballShade)" stroke="#c3ccd8" stroke-width="1.5"/>
    </svg>
    <p>Please put me on your notice board</p>
  </div>

  <p class="invitation">We invite our fellow Veteran Ladies and Gentlemen to<br>play a unique 54 hole stableford event at three<br>fantastic Golf Courses, and finish the week at Penwick<br>Golf club with a 2BBB Medley.</p>

  <div class="band band-dates">16th of October to 20th of October</div>
  <div class="band band-age">Over 55 years of age</div>

  <section class="program">
    <h2>PROGRAM</h2>
    <div class="row" style="top:39px"><span class="month">Oct</span><span class="date">15</span><span class="day">Sun</span><span class="detail">Penwick Golf Club - Registrations : 4.00pm - 6.00pm</span></div>
    <div class="row" style="top:79px"><span class="month">Oct</span><span class="date">16</span><span class="day">Mon</span><span class="detail">Dalbrook Golf Course Par 72 - Stableford - 1st Round Championships</span></div>
    <div class="row" style="top:119px"><span class="month">Oct</span><span class="date">17</span><span class="day">Tue</span><span class="detail">Marlow Golf Course Par 71 - HBVGA Trophy Day Stableford -<br>2nd Round Championships</span></div>
    <div class="row" style="top:174px"><span class="month">Oct</span><span class="date">18</span><span class="day">Wed</span><span class="detail">Leisure Day</span></div>
    <div class="row" style="top:214px"><span class="month">Oct</span><span class="date">19</span><span class="day">Thu</span><span class="detail">Ashgrove Golf Course Par 72 - Stableford - Round 3 Championships</span></div>
    <div class="row" style="top:254px"><span class="month">Oct</span><span class="date">20</span><span class="day">Fri</span><span class="detail">Penwick Golf Course Par 66 - 18 Hole 2BBB Medley Stableford<br>Penwick Golf Club ~ PRESENTATION DINNER DANCE ~ 7.00pm for 7.30pm</span></div>
  </section>

  <div class="courses">
    <div class="course course-1" role="img" aria-label="Photo of the first golf course fairway with hills"></div>
    <div class="course course-2" role="img" aria-label="Photo of the second golf course lined with trees"></div>
    <div class="course course-3" role="img" aria-label="Photo of the third golf course green with bunkers"></div>
    <div class="course course-4" role="img" aria-label="Photo of the fourth golf course green and clubhouse slope"></div>
  </div>
  <p class="tagline">Try our awesome golf courses for an amazing experience with everlasting memories</p>

  <footer class="contact">Contact: Penwick Proshop on 02 69318842 or email admin@penwickdalbrookgolf.example.au</footer>
</div>
</body>
</html>
```